Olive Oil Label Needs Graphic Designs

We need two sister label designs for 500ml bottles for our new brand "Casa Lumbre". Casa Lumbre is a high-end olive oil from Baeza, Spain which will be sold in the US. The oil will be produced from both Arbequina olives and Picual olives. Therefore, envisioning the same design just a different color scheme for the different labels.
The label should have the following characteristics; clean and simple, stand-out from mainstream labels, be eye-catching, give perception of high-end / high-quality.
Our current thinking of what we want (but please let your creative juices flow); lighter background, to be more eye catching, graphics of and olive, a olive branch or olive tree.
Text which should appear on the label are (not necessarily in this order);
Casa Lumbre
Extra Virgin Olive Oil
Family Reserve
Arbequina (One design)
Picual (Second design)
The label should be about 3 inches wide and 5.5 inches in height.

```html
<!DOCTYPE html>
<html lang="en">
<head>
<meta charset="utf-8">
<title>Casa Lumbre – Arbequina Label</title>
<link rel="stylesheet" href="https://fonts.googleapis.com/css2?family=Josefin+Sans:wght@300&family=Lora:ital@1&family=Yesteryear&display=swap">
<style>
  :root {
    --backdrop: #f3efe7;
    --label-lime: #c2da66;
    --label-lime-deep: #afcb4e;
    --ink-green: #3e6a2c;
    --frame-green: #4f7d36;
    --leaf-light: #a4c44a;
    --leaf-dark: #7ea23a;
  }
  html, body {
    margin: 0;
    padding: 0;
    width: 960px;
    height: 1200px;
    overflow: hidden;
    background: var(--backdrop);
  }
  .canvas {
    position: relative;
    width: 960px;
    height: 1200px;
  }
  .label {
    position: absolute;
    left: 263px;
    top: 32px;
    width: 434px;
    height: 1135px;
  }
  .label-shape {
    position: absolute;
    inset: 0;
  }
  .brand-dot {
    position: absolute;
    left: 184px;
    top: 126px;
    width: 66px;
    height: 66px;
    border-radius: 50%;
    background: var(--ink-green);
  }
  .brand-name {
    position: absolute;
    left: 0;
    width: 100%;
    top: 252px;
    margin: 0;
    text-align: center;
    font-family: "Josefin Sans", sans-serif;
    font-weight: 300;
    font-size: 50px;
    letter-spacing: 2px;
    color: var(--ink-green);
    line-height: 1;
  }
  .title-rule {
    position: absolute;
    left: 34px;
    width: 366px;
    top: 330px;
    height: 2px;
    background: var(--frame-green);
  }
  .variety {
    position: absolute;
    left: 0;
    width: 100%;
    top: 342px;
    margin: 0;
    text-align: center;
    font-family: "Lora", serif;
    font-style: italic;
    font-size: 21px;
    color: var(--ink-green);
  }
  .reserve {
    position: absolute;
    left: 0;
    width: 100%;
    top: 392px;
    margin: 0;
    text-align: center;
    font-family: "Yesteryear", cursive;
    font-size: 40px;
    color: var(--ink-green);
    line-height: 1;
  }
  .reserve-swash {
    position: absolute;
    left: 110px;
    top: 440px;
    width: 214px;
    height: 20px;
  }
  .branch-art {
    position: absolute;
    left: 14px;
    top: 474px;
    width: 406px;
    height: 546px;
    background: radial-gradient(ellipse at 60% 45%, var(--leaf-dark) 0%, var(--leaf-light) 55%, var(--label-lime) 100%);
    opacity: 0.85;
  }
  .volume {
    position: absolute;
    left: 0;
    width: 100%;
    top: 1036px;
    margin: 0;
    text-align: center;
    font-family: "Josefin Sans", sans-serif;
    font-weight: 300;
    font-size: 24px;
    color: var(--ink-green);
  }
</style>
</head>
<body>
<main class="canvas">
  <section class="label">
    <svg class="label-shape" width="434" height="1135" viewBox="0 0 434 1135" aria-hidden="true">
      <defs>
        <linearGradient id="labelFill" x1="0" y1="0" x2="0" y2="1">
          <stop offset="0" stop-color="var(--label-lime)"/>
          <stop offset="1" stop-color="var(--label-lime-deep)"/>
        </linearGradient>
      </defs>
      <polygon points="0,0 434,77 434,1135 0,1046" fill="url(#labelFill)"/>
      <polygon points="12,16 422,89 422,1118 12,1032" fill="none" stroke="var(--frame-green)" stroke-width="2.5"/>
    </svg>

    <span class="brand-dot" aria-hidden="true"></span>
    <h1 class="brand-name">CASA LUMBRE</h1>
    <span class="title-rule" aria-hidden="true"></span>
    <p class="variety">Extra Virgin Arbequina Olive Oil</p>
    <p class="reserve">Family Reserve</p>
    <svg class="reserve-swash" viewBox="0 0 214 20" aria-hidden="true">
      <path d="M4 6 Q107 22 210 6" fill="none" stroke="var(--ink-green)" stroke-width="2"/>
    </svg>

    <div class="branch-art" role="img" aria-label="Olive branch with leaves and olives in soft greens"></div>

    <p class="volume">500ml</p>
  </section>
</main>
</body>
</html>
```